"Lomi's" Website Design

Lomi's makes earth friendly, healthy, and delicious snacks that are completely gluten free. We are looking for a website that is easy to navigate, energetic, and conveys our purpose "To create healthy, earth-friendly, gluten free snacks that fill bellies and warm hearts."
Our first product is "Lomi's Crunch Rockets" are a small, square, cracker pack with an unreasonable amount of cheddar cheese flavor. The flavor literally explodes in your mouth!
We really want our site to pop and show off some personality.
I'm attaching the logo for the company, feel free to go beyond the logo in terms of color.
Here are some sites that we like!
http://www.frostvale-example.com/company
http://www.pebblemeal-example.com/
http://www.qv47-example.com/
http://www.dorsetloaf-example.com/
http://www.ventobite-example.com/food/products_zest/
http://www.marvelscoop-example.com/

```html
<!DOCTYPE html>
<html lang="en">
<head>
<meta charset="utf-8">
<title>Lomi's — For every taste bud</title>
<link rel="stylesheet" href="https://fonts.googleapis.com/css2?family=Arimo:wght@400&family=Gelasio:ital,wght@0,400;1,400;1,700&display=swap">
<style>
  :root {
    --page-bg: #f2f0f6;
    --panel-bg: #ffffff;
    --brand-orange: #f26522;
    --text-body: #3a3a3a;
    --nav-text: #3d3d3d;
    --link-blue: #5a9fd0;
    --rule-grey: #d8d6de;
    --wave-line: #e2e0e8;
    --bullet-olive: #c8b440;
  }
  * { margin: 0; padding: 0; box-sizing: border-box; }
  html, body {
    width: 1143px; height: 1200px; overflow: hidden;
    background: var(--page-bg);
  }
  .canvas { position: relative; width: 1143px; height: 1200px; }

  .site-header {
    position: absolute; left: 0; top: 0; width: 1143px; height: 116px;
  }
  .site-header svg { position: absolute; left: 0; top: 0; }
  .brand {
    position: absolute; left: 44px; top: 28px;
    font-family: "Gelasio", Georgia, serif; font-weight: 400;
    font-size: 44px; line-height: 52px; color: var(--brand-orange); letter-spacing: 1px;
  }
  .main-nav {
    position: absolute; left: 369px; top: 46px; width: 729px;
    display: flex; justify-content: space-between;
    font-family: "Gelasio", Georgia, serif; font-style: italic;
    font-size: 15px; line-height: 20px; color: var(--nav-text);
  }

  .hero-title {
    position: absolute; left: 67px; top: 170px; width: 520px;
    font-family: "Gelasio", Georgia, serif; font-style: italic; font-weight: 700;
    font-size: 55px; line-height: 51px; color: var(--brand-orange);
  }
  .hero-copy {
    position: absolute; left: 69px; top: 294px; width: 492px;
    font-family: "Arimo", Arial, sans-serif; font-size: 15px; line-height: 20.7px;
    color: var(--text-body);
  }
  .learn-more {
    position: absolute; left: 68px; top: 436px; width: 138px; height: 35px;
    border-top: 1px solid var(--rule-grey); border-bottom: 1px solid var(--rule-grey);
    display: flex; align-items: center; gap: 12px; padding-left: 4px;
    font-family: "Gelasio", Georgia, serif; font-style: italic;
    font-size: 20px; color: var(--link-blue);
  }
  .hero-visual {
    position: absolute; left: 567px; top: 104px; width: 551px; height: 430px;
    background: radial-gradient(ellipse at 55% 50%, #ffd36a 0%, #ffe7a8 45%, #fff1d0 68%, rgba(242,240,246,0) 85%);
  }

  .panel { position: absolute; left: 27px; width: 1091px; background: var(--panel-bg); }
  .panel-title {
    position: absolute;
    font-family: "Gelasio", Georgia, serif; font-style: italic; font-weight: 700;
    color: var(--brand-orange); line-height: 1.2;
  }
  .more-link {
    position: absolute;
    font-family: "Gelasio", Georgia, serif; font-style: italic;
    font-size: 16px; color: var(--link-blue);
  }

  .products { top: 542px; height: 264px; }
  .products .panel-title { left: 45px; top: 29px; font-size: 24px; }
  .product-thumb { position: absolute; top: 82px; width: 185px; height: 131px; }
  .thumb-feta { background: linear-gradient(135deg, #c9a07a, #f4f1ea 45%, #8a9a4a 80%, #c8452a); }
  .thumb-block { background: linear-gradient(135deg, #9c9a92, #eceae2 45%, #5b93c0 85%); }
  .thumb-yellow { background: linear-gradient(135deg, #d89a3a, #f6dc55 50%, #b8712a); }
  .thumb-blue { background: linear-gradient(135deg, #8a3a3a, #f3f0e6 45%, #e8a43a 90%); }
  .products .more-link { right: 36px; top: 231px; }

  .welcome { top: 813px; height: 285px; }
  .welcome .panel-title { left: 46px; top: 26px; font-size: 25px; }
  .welcome-copy {
    position: absolute; left: 47px; top: 64px; width: 668px;
    font-family: "Arimo", Arial, sans-serif; font-size: 15px; line-height: 20.7px;
    color: var(--text-body);
  }
  .welcome-copy p + p { margin-top: 10px; }
  .welcome .more-link { left: 631px; top: 244px; }
  .promo-poster {
    position: absolute; left: 834px; top: 12px; width: 236px; height: 262px;
    background: linear-gradient(180deg, #ddd07e 0%, #efe6a6 45%, #d8c66a 100%);
  }
  .promo-poster span {
    position: absolute; left: 0; right: 0; top: 36px; text-align: center;
    font-family: "Gelasio", Georgia, serif; font-size: 38px; color: var(--brand-orange);
  }

  .site-footer {
    position: absolute; left: 0; top: 1143px; width: 1143px; text-align: center;
    font-family: "Arimo", Arial, sans-serif; font-size: 11px; color: var(--text-body);
  }
</style>
</head>
<body>
<div class="canvas">

  <header class="site-header">
    <svg width="1143" height="116" viewBox="0 0 1143 116" aria-hidden="true">
      <path d="M0 0 H1143 V106 Q1115 98 1090 106 T1040 106 T990 106 T940 106 T890 106 T840 106 T790 106 T740 106 T690 106 T640 106 T590 106 T540 106 T490 106 T440 106 T390 106 T340 106 T290 106 T240 106 T190 106 T140 106 T90 106 T40 106 T0 106 Z"
            fill="#ffffff" stroke="var(--wave-line)" stroke-width="2"/>
    </svg>
    <div class="brand">Lomi's</div>
    <nav class="main-nav">
      <span>Our Mission</span>
      <span>Our Products</span>
      <span>Our Practices</span>
      <span>Recipes &amp; Fun</span>
      <span>School Gardens</span>
      <span>Contact us</span>
    </nav>
  </header>

  <section class="hero">
    <h1 class="hero-title">For every taste bud</h1>
    <p class="hero-copy">Lomi's makes earth friendly, healthy and delicious snacks that are completely gluten free. Our purpose is simple: to create healthy, earth-friendly, gluten free snacks that fill bellies and warm hearts. Meet Lomi's Crunch Rockets, small square cracker packs with an unreasonable amount of cheddar cheese flavor that literally explodes in your mouth!</p>
    <div class="learn-more">learn more
      <svg width="16" height="16" viewBox="0 0 16 16" aria-hidden="true">
        <circle cx="8" cy="8" r="7.5" fill="var(--bullet-olive)"/>
        <path d="M6.5 4.5 L10 8 L6.5 11.5" fill="none" stroke="#ffffff" stroke-width="1.8"/>
      </svg>
    </div>
    <div class="hero-visual" role="img" aria-label="Photo of rolled slices of Swiss cheese with holes"></div>
  </section>

  <section class="panel products">
    <h2 class="panel-title">Our Products</h2>
    <div class="product-thumb thumb-feta" style="left:43px" role="img" aria-label="Photo of white cheese blocks with tomatoes and a glass of wine"></div>
    <div class="product-thumb thumb-block" style="left:251px" role="img" aria-label="Photo of a white cheese block beside its package"></div>
    <div class="product-thumb thumb-feta" style="left:458px" role="img" aria-label="Photo of white cheese blocks with tomatoes and a glass of wine"></div>
    <div class="product-thumb thumb-yellow" style="left:666px" role="img" aria-label="Photo of yellow cheese slices on a board with a knife"></div>
    <div class="product-thumb thumb-blue" style="left:872px" role="img" aria-label="Photo of blue cheese with grapes, walnuts and basil"></div>
    <span class="more-link">view more</span>
  </section>

  <section class="panel welcome">
    <h2 class="panel-title">Welcome!</h2>
    <div class="welcome-copy">
      <p>Lomi's Crunch Rockets are our very first product: small, square crackers packed with an unreasonable amount of cheddar cheese flavor. Every bite bursts with cheesy goodness, and every pack is completely gluten free, made with simple ingredients and real care for the planet, so you can snack happily anywhere, anytime.</p>
      <p>We believe snacks should fill bellies and warm hearts. That is why everything we make is healthy, earth friendly and gluten free, from our kitchen all the way to your lunchbox.</p>
    </div>
    <span class="more-link">read more</span>
    <div class="promo-poster" role="img" aria-label="Promotional poster showing a cheese cracker sandwich and product packs">
      <span>Lomi's</span>
    </div>
  </section>

  <footer class="site-footer">© 2012 &nbsp;- Terms of Service - Privacy Policy - Program Policies</footer>

</div>
</body>
</html>
```